Brookvale Harbour Clinic advertising

I have a copy that we had done several years ago. I loved it and still do. Unfortunately, the original graphic designer lost the original artwork. What I do have is the same artwork at a small fridge magnet size. I need to new artwork to look like the small magnet version.
The main brief is to appeal to our clients who have addiction problems. It needs to be edgy and as far removed from the typical medical center images

Requirements
Must have
• The print quality must be able to be blown up to 1m x 2m.

```html
<!DOCTYPE html>
<html lang="en">
<head>
<meta charset="UTF-8">
<title>Brookvale Harbour Clinic – Heroin Treatment</title>
<link rel="stylesheet" href="https://fonts.googleapis.com/css2?family=Rubik+Dirt&family=Mulish:wght@300;400&display=swap">
<style>
  :root {
    --bg-deep: #150a18;
    --bg-mid: #23122a;
    --ink: #ffffff;
    --accent: #3dba7a;
    --skin-light: #e6dbcd;
    --skin-mid: #b49e8c;
    --skin-shade: #6e5258;
    --hair: #3a2430;
  }
  html, body {
    margin: 0;
    padding: 0;
    overflow: hidden;
    background: var(--bg-deep);
  }
  .ad {
    position: relative;
    width: 1200px;
    height: 600px;
    overflow: hidden;
    background: radial-gradient(ellipse at 30% 45%, var(--bg-mid) 0%, var(--bg-deep) 75%);
    font-family: "Mulish", sans-serif;
    color: var(--ink);
  }
  .portrait {
    position: absolute;
    left: 640px;
    top: 0;
    width: 560px;
    height: 600px;
  }
  .headline {
    position: absolute;
    left: 68px;
    top: 50px;
    margin: 0;
    font-family: "Rubik Dirt", sans-serif;
    font-weight: 400;
    font-size: 112px;
    line-height: 1;
    letter-spacing: -2px;
    color: var(--ink);
  }
  .tagline {
    position: absolute;
    left: 67px;
    top: 170px;
    margin: 0;
    font-weight: 300;
    font-size: 42px;
    line-height: 47px;
  }
  .phone {
    position: absolute;
    left: 63px;
    top: 360px;
    margin: 0;
    font-weight: 300;
    font-size: 68px;
    line-height: 1;
    letter-spacing: 1px;
    color: var(--accent);
  }
  .details {
    position: absolute;
    left: 67px;
    top: 430px;
    margin: 0;
    font-weight: 400;
    font-size: 35px;
    line-height: 39px;
  }
  .clinic-name { color: var(--accent); }
</style>
</head>
<body>
<main class="ad">
  <svg class="portrait" viewBox="0 0 560 600" role="img" aria-label="Photograph of a woman's face with dry, cracked skin and vivid green eyes, framed by a dark hood">
    <defs>
      <radialGradient id="skinTone" cx="0.58" cy="0.42" r="0.62">
        <stop offset="0" stop-color="var(--skin-light)"/>
        <stop offset="0.45" stop-color="var(--skin-mid)"/>
        <stop offset="0.8" stop-color="var(--skin-shade)"/>
        <stop offset="1" stop-color="var(--hair)"/>
      </radialGradient>
      <linearGradient id="hoodEdge" x1="0" x2="1">
        <stop offset="0" stop-color="var(--bg-deep)" stop-opacity="0"/>
        <stop offset="1" stop-color="var(--bg-deep)" stop-opacity="0.9"/>
      </linearGradient>
      <filter id="soften" x="-20%" y="-20%" width="140%" height="140%">
        <feGaussianBlur stdDeviation="16"/>
      </filter>
    </defs>
    <ellipse cx="120" cy="300" rx="110" ry="330" fill="var(--hair)" filter="url(#soften)" opacity="0.8"/>
    <ellipse cx="350" cy="250" rx="235" ry="330" fill="url(#skinTone)" filter="url(#soften)"/>
    <rect x="490" y="0" width="70" height="600" fill="url(#hoodEdge)"/>
  </svg>

  <h1 class="headline">HEROIN</h1>
  <p class="tagline">Got a problem?<br>We Can Help.</p>
  <p class="phone">9312 4860</p>
  <p class="details">
    <span class="clinic-name">Brookvale Harbour Clinic</span><br>
    Free Treatment Available<br>
    www.brookvaleharbour.com.au
  </p>
</main>
</body>
</html>
```